Business Card for Inovative Flexible Packaging Company

Create a business card that is both simple and stricking at the same time.
Preferably only one color (orange) or two colors (black and orange).
Information to print:
Torvalo, Lda
[T] 22 418 6093
[M] 91 326 7041
[F] 22 418 6135
[@] torvalo.ac@correiomx.com
SEDE & ARMAZÉM
Rua Das Figueiras do Monte, 312
Vale Lindo
4890-832 Vale Lindo - Montealto
PORTUGAL
Reason: A lot of the ideas are obvious. I want something different. Inovative. dare to do something eye catching with style.
Business Consumers. Packaging Designers.
Business

```html
<!DOCTYPE html>
<html lang="pt">
<head>
<meta charset="utf-8">
<title>Torvalo – Cartão de Visita</title>
<link rel="stylesheet" href="https://fonts.googleapis.com/css2?family=Roboto:wght@400;700&family=Roboto+Condensed:wght@400;700&display=swap">
<style>
  :root {
    --orange: #f26322;
    --white: #ffffff;
    --ink: #1a1a1a;
    --grey-text: #333333;
    --rule: #c8c8c8;
    --stage: #8e8e8e;
  }
  * { margin: 0; padding: 0; box-sizing: border-box; }
  html, body { width: 1200px; height: 2193px; overflow: hidden; background: var(--white); }
  body { position: relative; font-family: "Roboto", Arial, sans-serif; color: var(--ink); }

  /* Overview area: both sides side by side */
  .overview { position: absolute; left: 0; top: 0; width: 1200px; height: 855px; background: var(--stage); }
  .thumb { position: absolute; width: 480px; overflow: hidden; box-shadow: 0 6px 18px rgba(0,0,0,.25); }
  .thumb--front { left: 60px; top: 300px; height: 267px; }
  .thumb--back { left: 660px; top: 300px; height: 268px; }
  .thumb > .side { transform: scale(0.4); transform-origin: 0 0; position: absolute; left: 0; top: 0; }

  /* Full-size sides */
  .side { position: absolute; left: 0; width: 1200px; background: var(--white); }
  .side--front { top: 855px; height: 667px; }
  .side--back { top: 1523px; height: 670px; }
  .overview .side { top: 0; }

  .front-band { position: absolute; left: 0; top: 0; width: 1200px; height: 578px; background: var(--orange); }
  .brand-square { position: absolute; background: var(--white); }
  .front-band .brand-square { left: 110px; top: 178px; width: 200px; height: 200px; }
  .brand-name { position: absolute; font-weight: 700; line-height: 1; letter-spacing: -4px; white-space: nowrap; }
  .front-band .brand-name { left: 405px; top: 82px; font-size: 240px; color: var(--white); }
  .tagline { position: absolute; white-space: nowrap; font-weight: 400; text-transform: uppercase; }
  .front-band .tagline { left: 412px; top: 360px; font-size: 29px; letter-spacing: 15.2px; color: var(--white); }

  .web-strip { position: absolute; left: 0; top: 578px; width: 1200px; height: 89px; display: flex; align-items: center; justify-content: center; font-size: 45px; color: var(--grey-text); }
  .side--front::after { content: ""; position: absolute; left: 0; bottom: 0; width: 100%; height: 2px; background: var(--rule); }

  .back-square { position: absolute; left: 66px; top: 60px; width: 160px; height: 160px; background: var(--orange); }
  .back-name { position: absolute; left: 280px; top: 30px; font-size: 160px; font-weight: 700; line-height: 1; letter-spacing: -3px; color: var(--orange); white-space: nowrap; }
  .back-tagline { position: absolute; left: 283px; top: 197px; font-size: 20px; letter-spacing: 10.6px; color: var(--ink); text-transform: uppercase; white-space: nowrap; }

  .address { position: absolute; left: 66px; top: 360px; font-family: "Roboto Condensed", Arial, sans-serif; }
  .address-title { display: flex; align-items: center; gap: 8px; font-weight: 700; font-size: 38px; line-height: 1.2; }
  .address-title svg { width: 40px; height: 38px; }
  .address-lines { font-size: 32px; line-height: 45px; margin-top: 10px; }

  .contacts { position: absolute; right: 48px; top: 400px; font-family: "Roboto Condensed", Arial, sans-serif; font-size: 34px; }
  .phone-group { display: flex; align-items: flex-start; gap: 14px; justify-content: flex-end; }
  .phone-list { text-align: right; line-height: 45px; }
  .phone-group svg { width: 38px; height: 60px; margin-top: 2px; }
  .mail-row { display: flex; align-items: center; justify-content: flex-end; gap: 14px; margin-top: 32px; }
  .mail-row svg { width: 42px; height: 30px; }
</style>
</head>
<body>

<section class="overview" aria-label="Frente e verso do cartão">
  <div class="thumb thumb--front">
    <div class="side" style="height:667px">
      <div class="front-band">
        <div class="brand-square"></div>
        <div class="brand-name">torvalo</div>
        <div class="tagline">Flexible Pack Systems</div>
      </div>
      <div class="web-strip">www.torvalo.pt</div>
    </div>
  </div>
  <div class="thumb thumb--back">
    <div class="side" style="height:670px">
      <div class="back-square"></div>
      <div class="back-name">torvalo</div>
      <div class="back-tagline">Flexible Pack Systems</div>
      <div class="address">
        <div class="address-title">SEDE &amp; ARMAZÉM</div>
        <div class="address-lines">Rua Das Figueiras do Monte, 312<br>Vale Lindo<br>4890-832 Vale Lindo - Montealto<br>PORTUGAL</div>
      </div>
      <div class="contacts">
        <div class="phone-group"><div class="phone-list">22 418 6093<br>91 326 7041<br>22 418 6135</div></div>
        <div class="mail-row">torvalo.ac@correiomx.com</div>
      </div>
    </div>
  </div>
</section>

<section class="side side--front" aria-label="Frente do cartão">
  <div class="front-band">
    <div class="brand-square"></div>
    <div class="brand-name">torvalo</div>
    <div class="tagline">Flexible Pack Systems</div>
  </div>
  <div class="web-strip">www.torvalo.pt</div>
</section>

<section class="side side--back" aria-label="Verso do cartão">
  <div class="back-square"></div>
  <div class="back-name">torvalo</div>
  <div class="back-tagline">Flexible Pack Systems</div>

  <div class="address">
    <div class="address-title">
      <svg viewBox="0 0 40 38" aria-hidden="true">
        <circle cx="20" cy="8" r="6" fill="#1a1a1a"/>
        <rect x="18.5" y="12" width="3" height="14" fill="#1a1a1a"/>
        <path d="M3 22 L13 19 L27 23 L37 20 L37 36 L27 38 L13 34 L3 37 Z" fill="none" stroke="#1a1a1a" stroke-width="3" stroke-linejoin="round"/>
      </svg>
      SEDE &amp; ARMAZÉM
    </div>
    <div class="address-lines">
      Rua Das Figueiras do Monte, 312<br>
      Vale Lindo<br>
      4890-832 Vale Lindo - Montealto<br>
      PORTUGAL
    </div>
  </div>

  <div class="contacts">
    <div class="phone-group">
      <div class="phone-list">22 418 6093<br>91 326 7041<br>22 418 6135</div>
      <svg viewBox="0 0 38 60" aria-hidden="true">
        <rect x="3" y="2" width="32" height="56" rx="6" fill="none" stroke="#1a1a1a" stroke-width="4"/>
        <rect x="8" y="9" width="22" height="38" fill="#1a1a1a"/>
        <circle cx="19" cy="52" r="2.5" fill="#1a1a1a"/>
      </svg>
    </div>
    <div class="mail-row">
      torvalo.ac@correiomx.com
      <svg viewBox="0 0 42 30" aria-hidden="true">
        <rect x="2" y="2" width="38" height="26" rx="3" fill="none" stroke="#1a1a1a" stroke-width="4"/>
        <path d="M4 5 L21 17 L38 5" fill="none" stroke="#1a1a1a" stroke-width="4"/>
      </svg>
    </div>
  </div>
</section>

</body>
</html>
```